New Payments Start-up requires Logo, Style Guide and Web Site Design

We need a logo, style guide (colour templates etc.) and marketing web-site (HTML/CSS styling) for Kivex, a new account-to-account payment product for use in the Single European Payment Area (SEPA).

The design is for the product only, not a company brand. We're looking for basic palette and style guidelines also. The web site need only be a basic responsive cross-platform design and layout. We will produce our own content.

We have no requirements for specific colours or logo styles. It is a financial product, however, so should not appear too quirky or untrustworthy.

The product is still in the early phases of development, so we're not able to provide pictures or other content.

As a little more detail on how things work, though, our end customers will arrive at our site through redirection from our merchant partners (a number of whom are large multi-national companies) who have offered our services as an alternative to credit card payments. They will be able to set up a SEPA direct debit mandate online in just a few pages, secure that with a password and use it to pay both immediately and in future with a simple confirmation of the password… a quick, easy checkout.

Because we work with large customer in the payments space, whilst we’d like the brand to be modern and appealing, it has to engender trust and stability. Whilst this product is new and in start-up phase, our company has been in alternative payments for nearly 10 years and have strong products in Europe in the Pre-Paid Pelo/TrundlePay and Voucher space. We'd like to treat this separately, however, which is why we've briefed accordingly.

Project Deadline Extended
Reason: Apologies for the extension, but I had a couple of designers contact me to say they had completed work but were unable to submit because time ran out. I'll only extend this once, though, because we need to get cracking on the project. Many thanks Ben

Target Market(s)

European alternative payment customers

Industry/Entity Type

Financial

Logo Text

kivex

Coding

Coded - Design and coding required

Number of Pages Required

1 page

Font styles to use
Sans Serif

```html
<!DOCTYPE html>
<html lang="en">
<head>
<meta charset="utf-8">
<title>Kivex – Logo and Web Layout</title>
<link href="https://fonts.googleapis.com/css2?family=Lato:wght@300;400;700;900&display=swap" rel="stylesheet">
<style>
  :root {
    --brand-orange: #f05a28;
    --brand-yellow: #f2ea1d;
    --btn-blue: #2b3a8f;
    --btn-green: #1e7a3a;
    --ink-grey: #8a8a8a;
    --rule-grey: #d4d4d4;
    --mark-grey: #b5b5b5;
    --white: #ffffff;
    --overlay: rgba(38, 30, 28, 0.62);
  }
  * { box-sizing: border-box; margin: 0; padding: 0; }
  html, body { width: 800px; height: 1200px; overflow: hidden; background: var(--white); }
  body { position: relative; font-family: 'Lato', sans-serif; }

  /* Primary logo lockup */
  .logo-lockup { position: absolute; left: 262px; top: 100px; display: flex; align-items: center; gap: 14px; }
  .logo-lockup__dot { width: 62px; height: 62px; border-radius: 50%; background: var(--brand-orange); }
  .logo-lockup__name { font-weight: 900; font-size: 76px; line-height: 1; color: var(--brand-orange); letter-spacing: -2px; }

  /* Shared mockup pieces */
  .mockup { position: absolute; background: var(--white); overflow: hidden; }
  .mockup__header { position: absolute; left: 0; top: 0; width: 100%; background: var(--brand-orange); }
  .mockup__brand { position: absolute; font-weight: 900; color: var(--white); letter-spacing: -0.5px; line-height: 1; }
  .menu-toggle { position: absolute; display: flex; flex-direction: column; align-items: center; color: var(--white); }
  .menu-toggle__bars { display: flex; flex-direction: column; gap: 2px; }
  .menu-toggle__bars span { display: block; height: 2px; background: var(--white); }
  .menu-toggle__label { font-weight: 700; margin-top: 2px; }

  .hero { position: absolute; left: 0; width: 100%;
    background: linear-gradient(100deg, #c9c2c4 0%, #a89a96 22%, #5b4540 45%, #3a2a26 62%, #7a4a2e 82%, #b9652e 100%); }
  .hero__panel { position: absolute; background: var(--overlay); border-radius: 4px; text-align: center; color: var(--white); }
  .hero__title { font-weight: 400; line-height: 1.05; }
  .hero__tagline { font-weight: 900; color: var(--brand-yellow); }
  .btn { position: absolute; color: var(--white); border-radius: 2px; display: flex; align-items: center; justify-content: center; font-weight: 400; }
  .btn--login { background: var(--btn-blue); }
  .btn--register { background: var(--btn-green); }

  .banking { position: absolute; left: 0; width: 100%; background: var(--brand-orange); color: var(--white); text-align: center; }
  .banking__title { position: absolute; left: 0; width: 100%; font-weight: 700; }
  .banking__rule { position: absolute; height: 1px; background: var(--white); }
  .banking__text { position: absolute; left: 0; width: 100%; color: #ffc9b3; line-height: 1.4; }

  .footer-col { position: absolute; color: var(--ink-grey); line-height: 1.45; }
  .footer-mark { position: absolute; border-radius: 50%; background: var(--mark-grey); }
  .footer-bar { position: absolute; left: 0; width: 100%; background: var(--rule-grey); }

  /* Desktop */
  .mockup--desktop { left: 164px; top: 266px; width: 475px; height: 438px; }
  .mockup--desktop .mockup__header { height: 35px; }
  .mockup--desktop .mockup__brand { left: 15px; top: 7px; font-size: 21px; }
  .mockup--desktop .menu-toggle { left: 402px; top: 7px; }
  .mockup--desktop .menu-toggle__bars span { width: 22px; }
  .mockup--desktop .menu-toggle__label { font-size: 6px; }
  .mockup--desktop .hero { top: 35px; height: 254px; }
  .mockup--desktop .hero__panel { left: 270px; top: 81px; width: 166px; height: 78px; padding-top: 6px; }
  .mockup--desktop .hero__title { font-size: 16px; }
  .mockup--desktop .hero__tagline { font-size: 22px; margin-top: 5px; }
  .mockup--desktop .btn { top: 167px; height: 15px; font-size: 7.5px; }
  .mockup--desktop .btn--login { left: 302px; width: 42px; }
  .mockup--desktop .btn--register { left: 354px; width: 41px; }
  .mockup--desktop .banking { top: 289px; height: 74px; }
  .mockup--desktop .banking__title { top: 13px; font-size: 10.5px; }
  .mockup--desktop .banking__rule { top: 19px; width: 107px; }
  .mockup--desktop .banking__rule--left { left: 90px; }
  .mockup--desktop .banking__rule--right { left: 259px; }
  .mockup--desktop .banking__text { top: 32px; font-size: 4.6px; }
  .mockup--desktop .footer-col { top: 370px; font-size: 4.8px; width: 46px; }
  .mockup--desktop .footer-col--wide { width: 62px; }
  .mockup--desktop .footer-mark { left: 386px; top: 371px; width: 40px; height: 40px; }
  .mockup--desktop .footer-bar { top: 420px; height: 18px; }

  /* Mobile */
  .mockup--mobile { left: 284px; top: 789px; width: 237px; height: 366px; }
  .mockup--mobile .mockup__header { height: 28px; }
  .mockup--mobile .mockup__brand { left: 10px; top: 6px; font-size: 17px; }
  .mockup--mobile .menu-toggle { left: 188px; top: 5px; }
  .mockup--mobile .menu-toggle__bars span { width: 18px; }
  .mockup--mobile .menu-toggle__label { font-size: 5px; }
  .mockup--mobile .hero { top: 28px; height: 214px; }
  .mockup--mobile .hero__panel { left: 49px; top: 99px; width: 139px; height: 66px; padding-top: 5px; }
  .mockup--mobile .hero__title { font-size: 13.5px; }
  .mockup--mobile .hero__tagline { font-size: 19px; margin-top: 4px; }
  .mockup--mobile .btn { top: 173px; height: 21px; font-size: 10.5px; }
  .mockup--mobile .btn--login { left: 55px; width: 56px; }
  .mockup--mobile .btn--register { left: 125px; width: 56px; }
  .mockup--mobile .banking { top: 242px; height: 62px; }
  .mockup--mobile .banking__title { top: 10px; font-size: 9px; }
  .mockup--mobile .banking__text { top: 26px; font-size: 4px; }
  .mockup--mobile .footer-col { top: 309px; font-size: 4.4px; width: 34px; }
  .mockup--mobile .footer-mark { left: 172px; top: 310px; width: 34px; height: 34px; }
  .mockup--mobile .footer-bar { top: 351px; height: 15px; }
</style>
</head>
<body>

  <div class="logo-lockup">
    <div class="logo-lockup__dot"></div>
    <div class="logo-lockup__name">Kivex</div>
  </div>

  <section class="mockup mockup--desktop">
    <header class="mockup__header">
      <div class="mockup__brand">Kivex</div>
      <div class="menu-toggle">
        <div class="menu-toggle__bars"><span></span><span></span><span></span></div>
        <div class="menu-toggle__label">MENU</div>
      </div>
    </header>
    <div class="hero" role="img" aria-label="Photo of a smiling woman working at a laptop in a warm-lit office">
      <div class="hero__panel">
        <div class="hero__title">Account to account<br>payment Service</div>
        <div class="hero__tagline">Quick, Easy</div>
      </div>
      <div class="btn btn--login">LOG IN</div>
      <div class="btn btn--register">REGISTER</div>
    </div>
    <div class="banking">
      <div class="banking__rule banking__rule--left"></div>
      <div class="banking__title">Banking</div>
      <div class="banking__rule banking__rule--right"></div>
      <p class="banking__text">Pay straight from your bank account at checkout, safely and fast.<br>Set up once, confirm with a password, done.</p>
    </div>
    <p class="footer-col footer-col--wide" style="left:20px">Set up a direct debit mandate online in a few pages, secure it with a password and pay in one step.</p>
    <p class="footer-col" style="left:90px">Pay now or later with one simple password check.</p>
    <p class="footer-col" style="left:142px">Pay now or later with one simple password check.</p>
    <p class="footer-col" style="left:194px">Pay now or later with one simple password check.</p>
    <p class="footer-col" style="left:247px">Pay now or later with one simple password check.</p>
    <p class="footer-col" style="left:301px">Pay now or later with one simple password check.</p>
    <div class="footer-mark"></div>
    <div class="footer-bar"></div>
  </section>

  <section class="mockup mockup--mobile">
    <header class="mockup__header">
      <div class="mockup__brand">Kivex</div>
      <div class="menu-toggle">
        <div class="menu-toggle__bars"><span></span><span></span><span></span></div>
        <div class="menu-toggle__label">MENU</div>
      </div>
    </header>
    <div class="hero" role="img" aria-label="Photo of a smiling woman working at a laptop in a warm-lit office">
      <div class="hero__panel">
        <div class="hero__title">Account to account<br>payment Service</div>
        <div class="hero__tagline">Quick, Easy</div>
      </div>
      <div class="btn btn--login">LOG IN</div>
      <div class="btn btn--register">REGISTER</div>
    </div>
    <div class="banking">
      <div class="banking__title">Banking</div>
      <p class="banking__text">Pay straight from your bank account at checkout, safely and fast.<br>Set up once, confirm with a password, done.</p>
    </div>
    <p class="footer-col" style="left:26px">Pay now or later with one simple password check.</p>
    <p class="footer-col" style="left:79px">Pay now or later with one simple password check.</p>
    <div class="footer-mark"></div>
    <div class="footer-bar"></div>
  </section>

</body>
</html>
```